Corvane Real Estate Business Card

hello, we are a real estate company located in Los Angeles, california. we are a boutique, small company but we like a big corportate look. a simple, sleek, modern and progressive look. we would like the option of having a design that could include the real estate agents personal photo and also a design if the realtor desides not to have a photo. We also would like a hotizontal design.

Corvane Properties
3817 S Hadderly
West Hollywood, CA 90046
www.CorvaneRE.example

Gavin Prosk
Broker
BRE # 04829176
(555) 274-6390
gavin@corvanere.example

```html
<!DOCTYPE html>
<html lang="en">
<head>
<meta charset="utf-8">
<title>Corvane Real Estate Business Card</title>
<link rel="stylesheet" href="https://fonts.googleapis.com/css2?family=Arimo:wght@400;700&display=swap">
<style>
  :root {
    --stage: #121212;
    --card: #ffffff;
    --brand-blue: #1d4a8a;
    --ink: #1e1e1e;
    --photo-light: #c9cbb8;
    --photo-dark: #3c3a33;
  }
  * { margin: 0; padding: 0; box-sizing: border-box; }
  html, body {
    width: 1200px; height: 1082px; overflow: hidden;
    background: var(--stage);
    font-family: "Arimo", Arial, sans-serif;
  }
  .card {
    position: absolute; top: 214px;
    width: 379px; height: 659px;
    background: var(--card);
    text-align: center;
    color: var(--ink);
  }
  .card--front { left: 243px; }
  .card--back { left: 636px; }
  .agent-photo {
    position: absolute; left: 112px; top: 26px;
    width: 156px; height: 198px;
    border: 3px solid #fff;
    box-shadow: 0 1px 6px rgba(0,0,0,.45);
    background: linear-gradient(160deg, var(--photo-light) 0%, #8d8f78 45%, var(--photo-dark) 100%);
  }
  .brand {
    position: absolute; left: 0; right: 0; top: 278px;
    display: flex; justify-content: center; align-items: center; gap: 12px;
    color: var(--brand-blue);
    font-size: 44px; font-weight: 400; letter-spacing: -0.5px;
  }
  .brand__mark { width: 34px; height: 34px; background: var(--brand-blue); }
  .agent {
    position: absolute; left: 0; right: 0; top: 384px;
    font-size: 16px; line-height: 19px;
  }
  .agent__name { color: var(--brand-blue); font-size: 20px; font-weight: 700; line-height: 24px; }
  .office {
    position: absolute; left: 0; right: 0; top: 479px;
    font-size: 16px; line-height: 19px; font-style: normal;
  }
  .contact {
    position: absolute; left: 0; right: 0; top: 562px;
    list-style: none; font-size: 16px; line-height: 21px;
  }
  .contact li { display: flex; justify-content: center; align-items: center; gap: 7px; }
  .contact svg { width: 17px; height: 15px; fill: var(--brand-blue); }
</style>
</head>
<body>

<article class="card card--front">
  <div class="agent-photo" role="img" aria-label="Portrait photo of the agent"></div>
  <div class="brand"><span class="brand__mark"></span><span>Corvane</span></div>
  <div class="agent">
    <p class="agent__name">GAVIN PROSK</p>
    <p>BROKER</p>
    <p>BRE # 04829176</p>
  </div>
  <address class="office">
    <p>Corvane Properties</p>
    <p>3817 S Hadderly</p>
    <p>West Hollywood, CA 90046</p>
  </address>
  <ul class="contact">
    <li><svg viewBox="0 0 17 15"><path d="M1 5c2-3 13-3 15 0l-1 2-3-1V4H5v2L2 7zM4 8h9l2 6H2z"/></svg>(555) 274-6390</li>
    <li><svg viewBox="0 0 17 15"><path d="M1 2h15v11H1zM2.5 3.5 8.5 8l6-4.5v1.4l-6 4.5-6-4.5z" fill-rule="evenodd"/></svg>gavin@corvanere.example</li>
    <li><svg viewBox="0 0 17 15"><circle cx="8.5" cy="7.5" r="6.5" fill="none" stroke="#1d4a8a" stroke-width="1.4"/><path d="M2 7h13v1H2zM8 1h1v13H8z"/><ellipse cx="8.5" cy="7.5" rx="3" ry="6.5" fill="none" stroke="#1d4a8a"/></svg>www.CorvaneRE.example</li>
  </ul>
</article>

<article class="card card--back">
  <div class="agent-photo" role="img" aria-label="Portrait photo of the agent"></div>
  <div class="brand"><span class="brand__mark"></span><span>Corvane</span></div>
  <div class="agent">
    <p class="agent__name">GAVIN PROSK</p>
    <p>BROKER</p>
    <p>BRE # 04829176</p>
  </div>
  <address class="office">
    <p>Corvane Properties</p>
    <p>3817 S Hadderly</p>
    <p>West Hollywood, CA 90046</p>
  </address>
  <ul class="contact">
    <li><svg viewBox="0 0 17 15"><path d="M1 5c2-3 13-3 15 0l-1 2-3-1V4H5v2L2 7zM4 8h9l2 6H2z"/></svg>(555) 274-6390</li>
    <li><svg viewBox="0 0 17 15"><path d="M1 2h15v11H1zM2.5 3.5 8.5 8l6-4.5v1.4l-6 4.5-6-4.5z" fill-rule="evenodd"/></svg>gavin@corvanere.example</li>
    <li><svg viewBox="0 0 17 15"><circle cx="8.5" cy="7.5" r="6.5" fill="none" stroke="#1d4a8a" stroke-width="1.4"/><path d="M2 7h13v1H2zM8 1h1v13H8z"/><ellipse cx="8.5" cy="7.5" rx="3" ry="6.5" fill="none" stroke="#1d4a8a"/></svg>www.CorvaneRE.example</li>
  </ul>
</article>

</body>
</html>
```